Looking for an Innovative Print Design (Service Directory)

We need a new design for our advertisement within a printed colour services directory.

We are a compensation law firm called Velbrook Compensation Lawyers. Feel free to take a browse of our website www.velbrooklegal.com.au to get an idea of what we do and the kind of firm we are.

We are in the process of redeveloping our website and as such, so please don't adhere to the design principles of the current site- impress us with your originality!

On top of any editable formats, your final submissions must include a .pdf copy.
The same design will need to be presented in two dimensions:

- 154mm x 118mm (B1/B2 Half Page);
- 175mm x 113mm (B4 Half Page).

[For more information refer to attached Pdf.]

We have attached for you a few examples of other firms' designs (Sample1,2,3). These are by no means good, or what we're after, it's just to provide you with an idea of what sort of advertisements go into the service directory.

Hi all,

We want to emphasise that a priority of the design is that it must look:
• Professional
• Sophisticated
Please do not hesitate to use completely different colour schemes to the ones that are on our website- as we have said, our website will change in the near future, so cohesion between the current project and the website is not necessary!

Thanks!

Thank you for your submissions so far. There are some great ideas hidden in there. 

An issue we are having is that most of you are conforming to the same understanding of what it should look like. Remember that there is NO NEED to be bound by the image of firm as is. That is, feel free to use a different colour logo.

For inspiration, we relate well to the design aesthetics of: http://www.tinfernstudio.co.uk/

Look forward to seeing your 'out of the box' submissions. 

Reason: We've received a large amount of fantastic designs. However, what we're really looking for is something original. Please feel free to think outside the box (the final design doesn't need to look like a print ad), and construct a design that is completely incongruous with our website! While we do appreciate a minimalistic design, we have yet to receive something that really grabs your attention with its visuals. We're not sure but this may or may not be achieved with a full colour design. Thanks for all your submissions- they all have some features that really click with us. We look forward to the next wave of submissions!

Target Market(s)

We have various target markets, including mainly families, elderly people, blue collar workers.

These are individuals who are looking for assistance. They feel helpless or wronged.

Keep in mind that the people accessing these are those who prefer going to a printed directory rather than using a google search.

Industry/Entity Type

Law Firm

Font styles to use
Serif
Sans Serif

Requirements
Must have
• - Our name 'Velbrook Compensation Lawyers'
- Our logo (attached as logo.eps, logo.png, and logo.tif)
- Must include phone number as 1300 XXX XXX (this must be prominent)
- Must include the following service areas in these words: Motor vehicle claims, medical claims, superannuation claims, Workplace claims, negligence claims
- Our email address: info@velbrooklegal.com.au
- Our website address: www.velbrooklegal.com.au
- The following catchphrases: '98% success rate', and 'No win no fee' in those words
- Our location '412 Carvel Lane, Smithville, SYDNEY'
- For sizing dimensions, we need one in 154mm x 118mm and also a design in 175mm x 113mm (B4 Half Page) [refer to pdf attached]
Nice to have
• - Text indicating free initial consulatation
- Professional colour scheme
- As our website will be changed, do not worry about making the advertisement cohesive with our website design
- We want the design to be modern, but still professional
- Clean typeface
- No gradient colour scheme
- When designing, if you are looking to place more text onto the advertisement, these may be some considerations (feel free to change the wording): Accredited specialists, home and hospital visits

```html
<!DOCTYPE html>
<html lang="en">
<head>
<meta charset="utf-8">
<title>Velbrook Compensation Lawyers – Directory Advertisements</title>
<link rel="stylesheet" href="https://fonts.googleapis.com/css2?family=Asap+Condensed:ital,wght@0,400;0,500;1,400&family=Arimo:wght@400;700&display=swap">
<style>
  :root {
    --page: #ffffff;
    --frame: #3a3a3a;
    --ink: #58595b;
    --ink-dark: #2b2b2b;
    --steel: #7f9fb0;
    --mist: #d2d3d5;
    --band: #808184;
    --white: #ffffff;
    --icon: #7e9aab;
  }
  * { box-sizing: border-box; margin: 0; padding: 0; }
  html, body { width: 888px; height: 1200px; overflow: hidden; background: var(--page); }
  body { position: relative; font-family: "Asap Condensed", "Arial Narrow", sans-serif; color: var(--ink); }

  .ad { position: absolute; border: 1px solid var(--frame); background: var(--white); overflow: hidden; }
  .ad--half-b12 { left: 91px; top: 56px; width: 682px; height: 523px; }
  .ad--half-b4 { left: 56px; top: 643px; width: 776px; height: 500px; }

  .brand { position: absolute; display: flex; align-items: center; }
  .brand__dot { width: 86px; height: 86px; border-radius: 50%; background: var(--steel); flex: none; }
  .brand__name { margin-left: 16px; color: var(--ink); font-weight: 400; line-height: 1; }
  .brand__word { display: block; font-size: 44px; letter-spacing: 3px; }
  .brand__tag { display: block; font-size: 15.5px; letter-spacing: 2.6px; margin-top: 6px; }
  .ad--half-b12 .brand { left: 37px; top: 21px; }
  .ad--half-b4 .brand { left: 62px; top: 21px; }

  .photo { position: absolute; background: linear-gradient(100deg, #b79a86 0%, #d9d3cd 38%, #e4e9ec 55%, #3c4350 78%, #2a303a 100%); }
  .ad--half-b12 .photo { left: 458px; top: 0; width: 224px; height: 121px; }
  .ad--half-b4 .photo { left: 501px; top: 2px; width: 272px; height: 119px; }

  .benefits { position: absolute; background: var(--mist); display: flex; flex-direction: column; justify-content: center; align-items: center; list-style: none; }
  .benefits li { font-size: 26px; line-height: 41px; color: var(--ink); }
  .ad--half-b12 .benefits { left: 2px; top: 131px; width: 303px; height: 222px; }
  .ad--half-b4 .benefits { left: 3px; top: 132px; width: 354px; height: 208px; }

  .services { position: absolute; background: var(--steel); list-style: none; display: flex; flex-direction: column; justify-content: center; }
  .services li { color: var(--white); font-size: 31px; line-height: 39px; }
  .services li::before { content: "•"; margin-right: 12px; }
  .ad--half-b12 .services { left: 314px; top: 131px; width: 366px; height: 222px; padding-left: 22px; }
  .ad--half-b4 .services { left: 367px; top: 132px; width: 406px; height: 208px; padding-left: 26px; }
  .ad--half-b4 .services li { line-height: 37px; }

  .callout { position: absolute; background: var(--band); display: flex; align-items: center; justify-content: space-between; }
  .callout__phone { font-family: "Arimo", Arial, sans-serif; font-weight: 700; color: var(--white); letter-spacing: 0.5px; }
  .callout__offer { font-style: italic; color: var(--white); font-size: 25px; line-height: 26px; text-align: center; }
  .ad--half-b12 .callout { left: 2px; top: 361px; width: 678px; height: 84px; padding: 0 34px 0 20px; }
  .ad--half-b12 .callout__phone { font-size: 60px; }
  .ad--half-b4 .callout { left: 3px; top: 350px; width: 770px; height: 71px; padding: 0 26px 0 26px; }
  .ad--half-b4 .callout__phone { font-size: 55px; }

  .contact { position: absolute; left: 0; right: 0; font-family: "Arimo", Arial, sans-serif; font-size: 16px; color: var(--ink-dark); display: flex; flex-direction: column; align-items: center; gap: 7px; }
  .contact__row { display: flex; align-items: center; gap: 30px; }
  .contact__item { display: flex; align-items: center; gap: 8px; }
  .contact__web { font-weight: 700; }
  .contact svg { display: block; fill: var(--icon); }
  .ad--half-b12 .contact { top: 455px; }
  .ad--half-b4 .contact { top: 433px; }
</style>
</head>
<body>

<section class="ad ad--half-b12" aria-label="Half page advertisement, 154 by 118 mm">
  <div class="brand">
    <span class="brand__dot"></span>
    <span class="brand__name"><span class="brand__word">VELBROOK</span><span class="brand__tag">COMPENSATION LAWYERS</span></span>
  </div>
  <div class="photo" role="img" aria-label="Photo of a lawyer in a suit consulting with a client at a desk"></div>
  <ul class="benefits">
    <li>98% Success Rate!</li>
    <li>No win No fee</li>
    <li>Accredited Specialists</li>
    <li>Home and Hospital Visits</li>
  </ul>
  <ul class="services">
    <li>Motor vehicle claims</li>
    <li>Medical claims</li>
    <li>Superannuation claims</li>
    <li>Workplace claims</li>
    <li>Negligence claims</li>
  </ul>
  <div class="callout">
    <span class="callout__phone">1 300 XXX XXX</span>
    <span class="callout__offer">Free Initial<br>Consultation</span>
  </div>
  <div class="contact">
    <div class="contact__row">
      <span class="contact__item"><svg width="18" height="13" viewBox="0 0 18 13"><path d="M0 0h18v13H0z M1.5 1.5v10h15v-10L9 7.5z M2.5 1.5 9 6.2 15.5 1.5z" fill-rule="evenodd"/></svg>info@velbrooklegal.com.au</span>
      <span class="contact__item contact__web"><svg width="18" height="18" viewBox="0 0 18 18"><path d="M9 0a9 9 0 1 0 0 18A9 9 0 0 0 9 0zm0 1.4c.9 0 2 1.6 2.5 4.1h-5C7 3 8.1 1.4 9 1.4zM6.3 6.9h5.4a14 14 0 0 1 0 4.2H6.3a14 14 0 0 1 0-4.2zm-1.4 0a15 15 0 0 0 0 4.2H1.7a7.6 7.6 0 0 1 0-4.2zm8.2 0h3.2a7.6 7.6 0 0 1 0 4.2h-3.2a15 15 0 0 0 0-4.2zM2.3 5.5A7.6 7.6 0 0 1 6 1.9c-.6 1-1 2.2-1.3 3.6zm11 0c-.3-1.4-.7-2.6-1.3-3.6a7.6 7.6 0 0 1 3.7 3.6zM6.5 12.5h5c-.5 2.5-1.6 4.1-2.5 4.1s-2-1.6-2.5-4.1zm-4.2 0h2.4c.3 1.4.7 2.6 1.3 3.6a7.6 7.6 0 0 1-3.7-3.6zm11 0h2.4a7.6 7.6 0 0 1-3.7 3.6c.6-1 1-2.2 1.3-3.6z"/></svg>www.velbrooklegal.com.au</span>
    </div>
    <span class="contact__item"><svg width="14" height="19" viewBox="0 0 14 19"><path d="M7 0a7 7 0 0 0-7 7c0 5 7 12 7 12s7-7 7-12a7 7 0 0 0-7-7zm0 9.8A2.8 2.8 0 1 1 7 4.2a2.8 2.8 0 0 1 0 5.6z"/></svg>412 Carvel Lane, Smithville, SYDNEY</span>
  </div>
</section>

<section class="ad ad--half-b4" aria-label="Half page advertisement, 175 by 113 mm">
  <div class="brand">
    <span class="brand__dot"></span>
    <span class="brand__name"><span class="brand__word">VELBROOK</span><span class="brand__tag">COMPENSATION LAWYERS</span></span>
  </div>
  <div class="photo" role="img" aria-label="Photo of a lawyer in a suit consulting with a client at a desk"></div>
  <ul class="benefits">
    <li>98% Success Rate!</li>
    <li>No win No fee</li>
    <li>Accredited Specialists</li>
    <li>Home and Hospital Visits</li>
  </ul>
  <ul class="services">
    <li>Motor vehicle claims</li>
    <li>Medical claims</li>
    <li>Superannuation claims</li>
    <li>Workplace claims</li>
    <li>Negligence claims</li>
  </ul>
  <div class="callout">
    <span class="callout__phone">1 300 XXX XXX</span>
    <span class="callout__offer">Free Initial Consultation</span>
  </div>
  <div class="contact">
    <div class="contact__row">
      <span class="contact__item"><svg width="18" height="13" viewBox="0 0 18 13"><path d="M0 0h18v13H0z M1.5 1.5v10h15v-10L9 7.5z M2.5 1.5 9 6.2 15.5 1.5z" fill-rule="evenodd"/></svg>info@velbrooklegal.com.au</span>
      <span class="contact__item contact__web"><svg width="18" height="18" viewBox="0 0 18 18"><path d="M9 0a9 9 0 1 0 0 18A9 9 0 0 0 9 0zm0 1.4c.9 0 2 1.6 2.5 4.1h-5C7 3 8.1 1.4 9 1.4zM6.3 6.9h5.4a14 14 0 0 1 0 4.2H6.3a14 14 0 0 1 0-4.2zm-1.4 0a15 15 0 0 0 0 4.2H1.7a7.6 7.6 0 0 1 0-4.2zm8.2 0h3.2a7.6 7.6 0 0 1 0 4.2h-3.2a15 15 0 0 0 0-4.2zM2.3 5.5A7.6 7.6 0 0 1 6 1.9c-.6 1-1 2.2-1.3 3.6zm11 0c-.3-1.4-.7-2.6-1.3-3.6a7.6 7.6 0 0 1 3.7 3.6zM6.5 12.5h5c-.5 2.5-1.6 4.1-2.5 4.1s-2-1.6-2.5-4.1zm-4.2 0h2.4c.3 1.4.7 2.6 1.3 3.6a7.6 7.6 0 0 1-3.7-3.6zm11 0h2.4a7.6 7.6 0 0 1-3.7 3.6c.6-1 1-2.2 1.3-3.6z"/></svg>www.velbrooklegal.com.au</span>
    </div>
    <span class="contact__item"><svg width="14" height="19" viewBox="0 0 14 19"><path d="M7 0a7 7 0 0 0-7 7c0 5 7 12 7 12s7-7 7-12a7 7 0 0 0-7-7zm0 9.8A2.8 2.8 0 1 1 7 4.2a2.8 2.8 0 0 1 0 5.6z"/></svg>412 Carvel Lane, Smithville, SYDNEY</span>
  </div>
</section>

</body>
</html>
```